International sports company needs packaging design for color box

We need this box for our yoga mats which we will sell online. This mat is very high quality and 100% environmentally friendly. The yoga mat comes in a stylish yoga bag that will be in the box.

Yoga enthusiasts, athletes, gymnasts, actually all people who do sporting activities and value environmental friendliness will be the contact group

The logo should be visible in any case. The creator is free to choose whether to use only the complete logo or the complete logo with the emblem. In terms of style, it should be reminiscent of a packaging box from Corvane's Zentrix. Be as timeless, modern and elegant as possible. If an environmentally friendly detail can be added, this would certainly be a plus. Color should be black / white / gray.

Target Market(s)

Germany

Requirements
Must have
• Size for the color box should be 13x13x61.5 cm.

```html
<!DOCTYPE html>
<html lang="en">
<head>
<meta charset="utf-8">
<title>Solvera Yoga Mat Box</title>
<link rel="stylesheet" href="https://fonts.googleapis.com/css2?family=Open+Sans:wght@400;600;700&display=swap">
<style>
  :root {
    --stage: #858c92;
    --ink: #111111;
    --ink-side: #1b1b1b;
    --paper: #f4f4f4;
    --paper-side: #e2e2e2;
    --white: #ffffff;
    --mat-pink: #e0457f;
    --mat-violet: #9a7fd6;
    --mat-green: #b7c95a;
    --mat-orange: #e9842c;
    --mat-blue: #6c8fe0;
    --mat-plum: #7d3f78;
  }
  * { box-sizing: border-box; margin: 0; padding: 0; }
  html, body { width: 1200px; height: 789px; overflow: hidden; }
  body {
    background: var(--stage);
    font-family: "Open Sans", sans-serif;
    display: flex;
    align-items: center;
    justify-content: center;
    gap: 30px;
  }
  .box { width: 360px; display: flex; flex-direction: column; }
  .box__lid { position: relative; height: 440px; overflow: hidden; }
  .box__side {
    height: 150px;
    display: flex;
    align-items: center;
    justify-content: space-between;
    padding: 0 26px;
    border-top: 1px solid rgba(128,128,128,.35);
  }
  .box--black .box__lid { background: var(--ink); color: var(--white); }
  .box--black .box__side { background: var(--ink-side); color: var(--white); }
  .box--white .box__lid { background: var(--paper); color: var(--ink); }
  .box--white .box__side { background: var(--paper-side); color: var(--ink); }

  .wordmark {
    font-weight: 700;
    display: flex;
    align-items: center;
    gap: 10px;
    line-height: 1;
    white-space: nowrap;
  }
  .wordmark__square { width: 12px; height: 12px; background: currentColor; flex: none; }
  .box__lid .wordmark { position: absolute; left: 34px; bottom: 70px; font-size: 34px; }
  .box__side .wordmark { font-size: 22px; }

  .mat-photo { position: absolute; right: 0; top: 0; }
  .mat-photo--stack {
    width: 220px;
    height: 240px;
    background: linear-gradient(160deg, var(--mat-plum) 0%, var(--mat-pink) 30%, var(--mat-blue) 50%, var(--mat-green) 68%, var(--mat-orange) 84%, var(--mat-violet) 100%);
    border-radius: 0 0 0 60px;
  }
  .mat-photo--single {
    width: 190px;
    height: 300px;
    background: linear-gradient(165deg, #c3b0ee 0%, var(--mat-violet) 55%, #7a60bf 100%);
    border-radius: 0 0 0 95px;
  }

  .eco-badge { display: flex; align-items: center; gap: 8px; line-height: 1.1; }
  .eco-badge__leaf { width: 18px; height: 18px; fill: currentColor; flex: none; }
  .eco-badge__percent { font-weight: 700; font-size: 19px; display: block; }
  .eco-badge__line { font-size: 11px; display: block; }
  .eco-badge__friendly { font-size: 17px; font-weight: 600; display: block; }
</style>
</head>
<body>

<article class="box box--black">
  <section class="box__lid">
    <div class="mat-photo mat-photo--stack" role="img" aria-label="Photo of colourful rolled yoga mats stacked together"></div>
    <div class="wordmark"><span class="wordmark__square"></span>Solvera</div>
  </section>
  <section class="box__side">
    <div class="eco-badge">
      <svg class="eco-badge__leaf" viewBox="0 0 20 20" aria-hidden="true"><path d="M3 17C3 8 9 3 18 3c0 9-5 15-14 14zm1-1c3-4 6-7 10-9-4 1-8 4-10 9z"/></svg>
      <div>
        <span class="eco-badge__percent">100%</span>
        <span class="eco-badge__line">Environmentally</span>
        <span class="eco-badge__friendly">Friendly</span>
      </div>
    </div>
    <div class="wordmark"><span class="wordmark__square"></span>Solvera</div>
  </section>
</article>

<article class="box box--white">
  <section class="box__lid">
    <div class="mat-photo mat-photo--stack" role="img" aria-label="Photo of colourful rolled yoga mats stacked together"></div>
    <div class="wordmark"><span class="wordmark__square"></span>Solvera</div>
  </section>
  <section class="box__side">
    <div class="eco-badge">
      <svg class="eco-badge__leaf" viewBox="0 0 20 20" aria-hidden="true"><path d="M3 17C3 8 9 3 18 3c0 9-5 15-14 14zm1-1c3-4 6-7 10-9-4 1-8 4-10 9z"/></svg>
      <div>
        <span class="eco-badge__percent">100%</span>
        <span class="eco-badge__line">Environmentally</span>
        <span class="eco-badge__friendly">Friendly</span>
      </div>
    </div>
    <div class="wordmark"><span class="wordmark__square"></span>Solvera</div>
  </section>
</article>

<article class="box box--black">
  <section class="box__lid">
    <div class="mat-photo mat-photo--single" role="img" aria-label="Photo of a single lilac yoga mat partly unrolled"></div>
    <div class="wordmark"><span class="wordmark__square"></span>Solvera</div>
  </section>
  <section class="box__side">
    <div class="eco-badge">
      <svg class="eco-badge__leaf" viewBox="0 0 20 20" aria-hidden="true"><path d="M3 17C3 8 9 3 18 3c0 9-5 15-14 14zm1-1c3-4 6-7 10-9-4 1-8 4-10 9z"/></svg>
      <div>
        <span class="eco-badge__percent">100%</span>
        <span class="eco-badge__line">Environmentally</span>
        <span class="eco-badge__friendly">Friendly</span>
      </div>
    </div>
    <div class="wordmark"><span class="wordmark__square"></span>Solvera</div>
  </section>
</article>

</body>
</html>
```